BHSM Business Card Design Project

We are a Wedding Film company in Charleston, SC In need of a unique business card. Our website is www.brightharborstudiomedia.com. Check us out to get an idea of who we are and what we do. The design should be upscale but not pretentious. Modern but not cheesy. I will most likely have our cards printed by Zell on the Plume design. I'm also liking the raised designs for our logo. The Wedding Films in our logo on our site is blue so feel free to manipulate our logo for your designs as well.

Industry/Entity Type

Business

Requirements
Must have
• This is the info I want on the card:

Derek Halloway
Storyteller

Brightharbor Studio Media
www.brightharborstudiomedia.com

843.627.4150
derek@brightharborstudiomedia.com

```html
<!DOCTYPE html>
<html lang="en">
<head>
<meta charset="utf-8">
<title>Brightharbor Studio Media – Business Card</title>
<link rel="stylesheet" href="https://fonts.googleapis.com/css2?family=Raleway:wght@400;500&family=Arimo:wght@400&display=swap">
<style>
  :root {
    --stage: #e4e4e4;
    --gold: #9a8452;
    --gold-dark: #85703f;
    --gold-light: #cdbd82;
    --paper: #ffffff;
    --blue: #2b7fc3;
    --shadow: rgba(0, 0, 0, 0.18);
  }
  * { margin: 0; padding: 0; box-sizing: border-box; }
  html, body {
    width: 1200px;
    height: 900px;
    overflow: hidden;
    background: var(--stage);
  }
  .stage {
    position: relative;
    width: 1200px;
    height: 900px;
  }
  .card {
    position: absolute;
    left: 250px;
    width: 700px;
    height: 400px;
    overflow: hidden;
    box-shadow: 0 6px 18px var(--shadow);
  }
  .card--back {
    top: 30px;
    background: radial-gradient(ellipse 55% 60% at 50% 30%, var(--gold-light) 0%, var(--gold) 60%, var(--gold-dark) 100%);
  }
  .card--front {
    top: 470px;
    background: var(--paper);
  }

  /* back side */
  .back-band {
    position: absolute;
    left: 0;
    top: 190px;
    width: 100%;
    height: 100px;
    background: var(--paper);
    display: flex;
    align-items: center;
    justify-content: center;
    gap: 16px;
  }
  .brand-name {
    font-family: "Raleway", sans-serif;
    font-weight: 400;
    color: var(--gold);
    white-space: nowrap;
  }
  .back-band .brand-name {
    font-size: 40px;
    letter-spacing: 1px;
  }
  .brand-dot {
    width: 14px;
    height: 14px;
    border-radius: 50%;
    background: var(--gold);
  }
  .back-web {
    position: absolute;
    left: 0;
    top: 308px;
    width: 100%;
    text-align: center;
    font-family: "Arimo", sans-serif;
    font-size: 15px;
    letter-spacing: 1px;
    color: var(--paper);
  }

  /* front side */
  .front-brand {
    position: absolute;
    left: 0;
    top: 95px;
    width: 100%;
    text-align: center;
  }
  .front-brand .brand-name {
    font-size: 30px;
    letter-spacing: 1px;
  }
  .name-band {
    position: absolute;
    left: 0;
    top: 212px;
    width: 100%;
    height: 58px;
    background: linear-gradient(180deg, var(--gold) 0%, var(--gold-dark) 100%);
    display: flex;
    align-items: center;
    justify-content: center;
  }
  .person-name {
    font-family: "Raleway", sans-serif;
    font-weight: 500;
    font-size: 27px;
    letter-spacing: 4px;
    text-transform: uppercase;
    color: var(--paper);
  }
  .role {
    position: absolute;
    left: 0;
    top: 288px;
    width: 100%;
    text-align: center;
    font-family: "Raleway", sans-serif;
    font-weight: 500;
    font-size: 18px;
    letter-spacing: 3px;
    text-transform: uppercase;
    color: var(--blue);
  }
  .contact {
    position: absolute;
    left: 0;
    top: 326px;
    width: 100%;
    text-align: center;
    font-family: "Arimo", sans-serif;
    font-size: 14px;
    line-height: 22px;
    color: var(--blue);
  }
  .contact .sep { margin: 0 8px; }
</style>
</head>
<body>
  <main class="stage">
    <section class="card card--back" aria-label="Card back">
      <div class="back-band">
        <span class="brand-dot"></span>
        <span class="brand-name">Brightharbor Studio Media</span>
      </div>
      <p class="back-web">www.brightharborstudiomedia.com</p>
    </section>

    <section class="card card--front" aria-label="Card front">
      <div class="front-brand">
        <span class="brand-name">Brightharbor Studio Media</span>
      </div>
      <div class="name-band">
        <h1 class="person-name">Derek Halloway</h1>
      </div>
      <p class="role">Storyteller</p>
      <div class="contact">
        <p>Brightharbor Studio Media<span class="sep">|</span>derek@brightharborstudiomedia.com<span class="sep">|</span>843.627.4150</p>
        <p>www.brightharborstudiomedia.com</p>
      </div>
    </section>
  </main>
</body>
</html>
```